Vietnam Motorcycle Trip TRAVEL GUIDE!! Book Cover!

I need an adventurous book cover for a book called "THROTTLE SAGA: A Drifter's Handbook to Crossing the Spine of Vietnam". I would like people to look at the cover and think adventure and Vietnam. I want it to appeal to backpackers and people who have not travelled to Vietnam. A motorbike riding along a road in Vietnam would be ideal with some landscapes to suggest we are definitely in Vietnam. The rear cover could perhaps be one of Vietnam's tropical beaches or something else that says "this place is a paradise". It could also be something else that is quinessentially Vietnamese.

The book will be A5 Dimensions. And it will also need a printable A5 interior cover too. The interior covers can just be images. No text needed. These interior images can be motorcycle related or Vietnam related. Perhaps some images of Vietnam or some Pho or Banh Mi to give it a bit of flavour. Or a long open road with a motorbike on it.

Please leave space in the external rear, lower right hand corner for a barcode.

I've attached some images to gain inspiration from. And a sample chapter.

Colours I'd like to see on there - greens, camoflague perhaps, yellow, brown, blue.

Target Market(s)

Male backpackers aged 18-35 years old. New Zealand and Australian travellers.

Font styles to use
Serif
Sans Serif

Requirements
Must have
• Exterior and Interior covers.
Barcode space.
Title and subtitle.
Synopsis on rear cover.
Exciting title fonts - perhaps Brushstroke or something equally exciting and rugged
Nice to have
• Colours I'd like to see on there - greens, camoflague perhaps, yellow, brown, blue.

A motorbike riding on the open road of Vietnam.

Rice paddies, beaches, Vietnam War stuff perhaps.

A New Zealand Flag
A Vietnam Flag
Should not have
• Scenery from countries outside Southeast Asia

```html
<!DOCTYPE html>
<html lang="en">
<head>
<meta charset="utf-8">
<title>Throttle Saga – Book Cover</title>
<link rel="stylesheet" href="https://fonts.googleapis.com/css2?family=Josefin+Sans:wght@600;700&family=Open+Sans:wght@400;700&display=swap">
<style>
  :root {
    --backdrop: #d8dadd;
    --cover-yellow: #e6c02b;
    --title-white: #ffffff;
    --title-yellow: #f0c92c;
    --ink: #1b1b1b;
    --forest-dark: #3f5a34;
    --forest-mid: #6f8f4a;
    --mist: #b9c3b8;
    --road-grey: #8d918f;
    --paper-light: #f1f2f3;
    --paper-grey: #c9cbcd;
    --photo-dark: #2f3133;
    --photo-mid: #8a8c8e;
  }
  * { box-sizing: border-box; margin: 0; padding: 0; }
  html, body { width: 1200px; height: 900px; overflow: hidden; }
  body {
    background: var(--backdrop);
    font-family: "Open Sans", sans-serif;
    position: relative;
  }
  .cover {
    position: absolute;
    top: 170px;
    width: 380px;
    height: 540px;
    background: var(--cover-yellow);
    box-shadow: 0 10px 30px rgba(0,0,0,0.15);
  }
  .cover--front { left: 170px; }
  .cover--back { left: 650px; }

  /* Front */
  .front-photo {
    position: absolute;
    left: 14px; top: 14px; right: 14px; bottom: 62px;
    background:
      linear-gradient(115deg, transparent 55%, var(--mist) 85%),
      linear-gradient(160deg, var(--forest-dark) 0%, var(--forest-mid) 45%, var(--road-grey) 62%, var(--forest-mid) 78%, var(--forest-dark) 100%);
    overflow: hidden;
  }
  .front-subtitle {
    position: absolute;
    left: 22px; top: 26px;
    width: 190px;
    font-family: "Josefin Sans", sans-serif;
    font-weight: 600;
    font-size: 12.5px;
    line-height: 1.1;
    letter-spacing: 0.04em;
    color: var(--title-white);
    text-transform: uppercase;
  }
  .title {
    font-family: "Josefin Sans", sans-serif;
    font-weight: 700;
    text-transform: uppercase;
  }
  .title-main {
    position: absolute;
    left: 20px; top: 78px;
    font-size: 52px;
    line-height: 1;
    letter-spacing: 0.01em;
    color: var(--title-white);
  }
  .title-main .accent { color: var(--title-yellow); }
  .title-vertical {
    position: absolute;
    left: 56px; top: 138px;
    display: flex;
    flex-direction: column;
    align-items: center;
    font-size: 64px;
    line-height: 0.98;
    color: var(--title-yellow);
  }
  .front-author {
    position: absolute;
    left: 0; right: 0; bottom: 20px;
    text-align: center;
    font-family: "Josefin Sans", sans-serif;
    font-weight: 700;
    font-size: 14px;
    letter-spacing: 0.04em;
    color: var(--ink);
    text-transform: uppercase;
  }

  /* Back */
  .back-panel {
    position: absolute;
    left: 14px; top: 14px; right: 14px; bottom: 14px;
    background: linear-gradient(180deg, var(--paper-light) 0%, var(--paper-grey) 100%);
    overflow: hidden;
  }
  .synopsis {
    position: absolute;
    left: 22px; right: 22px; top: 30px;
    font-size: 9.6px;
    line-height: 1.32;
    color: var(--ink);
  }
  .synopsis p { margin-bottom: 9px; }
  .synopsis .lead { font-weight: 700; margin-bottom: 12px; }
  .synopsis .closer { font-weight: 700; }
  .back-photo {
    position: absolute;
    left: 0; right: 0; bottom: 0;
    height: 268px;
    background:
      linear-gradient(180deg, var(--paper-grey) 0%, var(--photo-mid) 22%, var(--photo-dark) 60%, var(--photo-mid) 100%);
  }
</style>
</head>
<body>

  <section class="cover cover--front">
    <div class="front-photo" role="img" aria-label="A motorcyclist riding a winding road up a lush green mountainside in northern Vietnam"></div>
    <p class="front-subtitle">A Drifter's Handbook to Crossing the Spine of Vietnam</p>
    <h1 class="title">
      <span class="title-main">T<span class="accent">H</span>ROTTLE</span>
      <span class="title-vertical" aria-label="Saga"><span>S</span><span>A</span><span>G</span><span>A</span></span>
    </h1>
    <p class="front-author">By Callum Hartwell</p>
  </section>

  <section class="cover cover--back">
    <div class="back-panel">
      <div class="synopsis">
        <p class="lead">Travel like a pro in a country where bribing cops is normal!</p>
        <p>Everyone knows someone who's ridden the length of Vietnam. What if you could do the same? For us Kiwis and Australians, it's difficult finding decent material about motorcycling in Vietnam. With so much conflicting information online and uncertainty around costs, it's no wonder people keep putting off this 1600 km road trip.</p>
        <p>Cal Hartwell has been there and done it. In the flesh. And whether your goal is riding from Saigon to Hanoi, across multiple Southeast Asian countries, or just hooning around for a few days, this guide is your bulletproof vest. It reveals</p>
        <p class="closer">None of us are getting any younger. And with all the information you need in one lightweight book, what's stopping you?</p>
      </div>
      <div class="back-photo" role="img" aria-label="Black and white rider's view over motorcycle handlebars and mirrors down an open highway toward mountains"></div>
    </div>
  </section>

</body>
</html>
```